Modern Lawfirm Business Card Design

We're looking for a business card to incorporate the newly created logo we had made.

Ideally looking for a law firm business card demonstrating, modern, minimalist, strong/bold design.

I'm open to any design honestly, but nothing "flashy".

Target Market(s)

Immigration law, family immigration, humanitarian, general legal

Industry/Entity Type

Law Firm

Contact Information for Business Card

Please use dummy information, name, street address, city, state, phone number, email, website.

Font styles to use
Serif
Sans Serif

Requirements
Must have
• Please use dummy information, name, street address, city, state, phone number, email, website.

```html
<!DOCTYPE html>
<html lang="en">
<head>
<meta charset="utf-8">
<title>Valdera Immigration Law – Business Card</title>
<link href="https://fonts.googleapis.com/css2?family=Open+Sans:wght@400;600;700&display=swap" rel="stylesheet">
<style>
  :root {
    --navy: #1d4a85;
    --navy-text: #1f5ba6;
    --swoosh: #76787b;
    --paper: #ffffff;
    --ink-grey: #5f6164;
    --backdrop: #e4e5e7;
  }
  * { box-sizing: border-box; margin: 0; padding: 0; }
  html, body {
    width: 1200px; height: 1000px; overflow: hidden;
    background: var(--backdrop);
    font-family: "Open Sans", sans-serif;
  }
  .stage { position: relative; width: 1200px; height: 1000px; }
  .card {
    position: absolute; left: 250px; width: 700px; height: 400px;
    overflow: hidden;
    box-shadow: 0 6px 18px rgba(0,0,0,0.18);
  }
  .card--back { top: 60px; background: var(--navy); }
  .card--front { top: 540px; background: var(--paper); }

  .wordmark {
    font-weight: 700;
    letter-spacing: 0.06em;
    text-transform: uppercase;
    line-height: 1.05;
  }
  .wordmark__name { display: block; font-size: 46px; }
  .wordmark__sub { display: block; font-size: 14px; letter-spacing: 0.42em; }

  .card--back .wordmark {
    position: absolute; left: 0; right: 0; top: 150px;
    text-align: center; color: var(--paper);
  }

  .card--front .wordmark {
    position: absolute; left: 40px; top: 34px; color: var(--navy-text);
  }
  .card--front .wordmark__name { font-size: 40px; }
  .card--front .wordmark__sub { font-size: 12px; }

  .front-shapes { position: absolute; inset: 0; }

  .person { position: absolute; left: 130px; top: 138px; }
  .person__name { font-size: 30px; font-weight: 700; color: var(--navy-text); line-height: 1.1; }
  .person__title { font-size: 17px; font-weight: 400; color: var(--ink-grey); margin-top: 2px; }

  .contact {
    position: absolute; right: 34px; top: 294px;
    list-style: none; color: var(--paper);
    font-size: 17px; line-height: 23px; text-align: right;
  }
  .contact__item { display: flex; justify-content: flex-end; align-items: center; gap: 12px; white-space: nowrap; }
  .contact__icon { width: 15px; height: 15px; flex: none; }
  .contact__item--plain { padding-right: 27px; }
</style>
</head>
<body>
<main class="stage">
  <section class="card card--back" aria-label="Card back">
    <div class="wordmark">
      <span class="wordmark__name">Valdera</span>
      <span class="wordmark__sub">Immigration Law</span>
    </div>
  </section>

  <section class="card card--front" aria-label="Card front">
    <svg class="front-shapes" viewBox="0 0 700 400" width="700" height="400" aria-hidden="true">
      <path d="M0,222 C130,268 330,292 700,290 L700,400 L0,400 Z" fill="var(--navy)"/>
      <path d="M30,196 C170,246 360,268 700,266 L700,280 C360,280 170,256 30,196 Z" fill="var(--swoosh)"/>
    </svg>

    <div class="wordmark">
      <span class="wordmark__name">Valdera</span>
      <span class="wordmark__sub">Immigration Law</span>
    </div>

    <div class="person">
      <p class="person__name">Adrian Castell</p>
      <p class="person__title">Founder/CEO</p>
    </div>

    <ul class="contact">
      <li class="contact__item">000 555 0192
        <svg class="contact__icon" viewBox="0 0 16 16" aria-hidden="true"><path d="M3.5 1.5l2.5 0 1 3.5-1.6 1.2c.8 1.8 2.2 3.2 4 4l1.2-1.6 3.4 1v2.5c0 .8-.7 1.4-1.5 1.4C6.8 13.5 2.5 9.2 2 3c0-.8.7-1.5 1.5-1.5z" fill="currentColor"/></svg>
      </li>
      <li class="contact__item">info@valderalaw.com
        <svg class="contact__icon" viewBox="0 0 16 16" aria-hidden="true"><rect x="1" y="3" width="14" height="10" fill="currentColor"/><path d="M1.5 3.5L8 9l6.5-5.5" stroke="var(--navy)" stroke-width="1.3" fill="none"/></svg>
      </li>
      <li class="contact__item">www.valderalaw.com
        <svg class="contact__icon" viewBox="0 0 16 16" aria-hidden="true"><circle cx="8" cy="8" r="6.5" fill="none" stroke="currentColor" stroke-width="1.4"/><ellipse cx="8" cy="8" rx="2.8" ry="6.5" fill="none" stroke="currentColor" stroke-width="1.2"/><path d="M1.5 8h13M2.5 4.8h11M2.5 11.2h11" stroke="currentColor" stroke-width="1.1"/></svg>
      </li>
      <li class="contact__item contact__item--plain">48 Harbour Street, Singapore, 5678</li>
    </ul>
  </section>
</main>
</body>
</html>
```